Answer Choice Icons

We need four versions of an answer choice icon. We need an A, B, C and D. They need to be 40 by 40 pixels and in .png format. They will be used as the labels for the answer choices on a multiple choice test. The student will click on the A, the B, the C, or D icon to select their answer. I have uploaded an example.

Industry/Entity Type

Student

Requirements
Must have
• 40 x 40 pixels; png format
Nice to have
• An oval shape with some shine would be nice. Also having each one a different color would be good.

```html
<!DOCTYPE html>
<html lang="en">
<head>
<meta charset="utf-8">
<title>Find the area of the rectangle</title>
<link href="https://fonts.googleapis.com/css2?family=Open+Sans:wght@400;700&display=swap" rel="stylesheet">
<style>
  :root {
    --page: #ffffff;
    --ink: #2b2b2b;
    --tile: #8c4dff;
    --grid-line: #111111;
    --red-dark: #8e0c10;
    --red: #d3262b;
    --blue-dark: #17569e;
    --blue: #4ea2ee;
    --gold-dark: #c57a06;
    --gold: #f7bf2a;
    --green-dark: #1f6a1a;
    --green: #4bac3b;
    --silver-light: #f4f4f4;
    --silver-dark: #9a9a9a;
  }
  * { margin: 0; padding: 0; box-sizing: border-box; }
  html, body { width: 1200px; height: 1200px; overflow: hidden; background: var(--page); }
  body { position: relative; font-family: "Open Sans", Arial, sans-serif; color: var(--ink); }

  .question { position: absolute; left: 126px; top: 20px; font-size: 26px; }
  .question-label { font-weight: 700; }

  .area-grid { position: absolute; left: 891px; top: 86px; }

  .legend { position: absolute; left: 825px; top: 645px; display: flex; align-items: center; gap: 12px; font-size: 27px; }
  .legend-tile { width: 53px; height: 53px; background: var(--tile); border: 3px solid var(--grid-line); }

  .choices { position: absolute; left: 92px; top: 742px; list-style: none; }
  .choice { display: flex; align-items: center; height: 109px; margin-top: -1px; }
  .choice-badge { width: 152px; height: 82px; flex: none; }
  .choice-text { font-size: 27px; margin-left: 10px; }
  .badge-letter { font-family: "Open Sans", Arial, sans-serif; font-weight: 700; font-size: 56px; }
</style>
</head>
<body>
  <p class="question"><span class="question-label">Question:</span> Find the area of the rectangle.</p>

  <svg class="area-grid" width="156" height="510" viewBox="0 0 156 510" aria-label="Rectangle made of 3 by 10 unit squares">
    <rect x="1.5" y="1.5" width="153" height="507" fill="var(--tile)" stroke="var(--grid-line)" stroke-width="3"/>
    <g stroke="var(--grid-line)" stroke-width="3">
      <line x1="52.5" y1="0" x2="52.5" y2="510"/>
      <line x1="103.5" y1="0" x2="103.5" y2="510"/>
      <line x1="0" y1="52.2" x2="156" y2="52.2"/>
      <line x1="0" y1="102.9" x2="156" y2="102.9"/>
      <line x1="0" y1="153.6" x2="156" y2="153.6"/>
      <line x1="0" y1="204.3" x2="156" y2="204.3"/>
      <line x1="0" y1="255" x2="156" y2="255"/>
      <line x1="0" y1="305.7" x2="156" y2="305.7"/>
      <line x1="0" y1="356.4" x2="156" y2="356.4"/>
      <line x1="0" y1="407.1" x2="156" y2="407.1"/>
      <line x1="0" y1="457.8" x2="156" y2="457.8"/>
    </g>
  </svg>

  <div class="legend"><span class="legend-tile"></span><span class="legend-text">= 1 square meter</span></div>

  <svg width="0" height="0" style="position:absolute">
    <defs>
      <radialGradient id="fill-red" cx="50%" cy="35%" r="65%"><stop offset="0" stop-color="var(--red)"/><stop offset="1" stop-color="var(--red-dark)"/></radialGradient>
      <radialGradient id="fill-blue" cx="50%" cy="35%" r="65%"><stop offset="0" stop-color="var(--blue)"/><stop offset="1" stop-color="var(--blue-dark)"/></radialGradient>
      <radialGradient id="fill-gold" cx="50%" cy="35%" r="65%"><stop offset="0" stop-color="var(--gold)"/><stop offset="1" stop-color="var(--gold-dark)"/></radialGradient>
      <radialGradient id="fill-green" cx="50%" cy="35%" r="65%"><stop offset="0" stop-color="var(--green)"/><stop offset="1" stop-color="var(--green-dark)"/></radialGradient>
      <linearGradient id="shine" x1="0" y1="0" x2="0" y2="1"><stop offset="0" stop-color="#fff" stop-opacity="0.75"/><stop offset="1" stop-color="#fff" stop-opacity="0"/></linearGradient>
      <linearGradient id="silver" x1="0" y1="0" x2="0" y2="1"><stop offset="0" stop-color="var(--silver-light)"/><stop offset="0.5" stop-color="#cfcfcf"/><stop offset="1" stop-color="var(--silver-dark)"/></linearGradient>
      <radialGradient id="drop" cx="50%" cy="50%" r="50%"><stop offset="0" stop-color="#000" stop-opacity="0.25"/><stop offset="1" stop-color="#000" stop-opacity="0"/></radialGradient>
    </defs>
  </svg>

  <ul class="choices">
    <li class="choice">
      <svg class="choice-badge" viewBox="0 0 152 82" aria-label="Choice A">
        <ellipse cx="76" cy="74" rx="66" ry="7" fill="url(#drop)"/>
        <ellipse cx="76" cy="38" rx="72" ry="34" fill="url(#fill-red)"/>
        <ellipse cx="76" cy="20" rx="54" ry="14" fill="url(#shine)"/>
        <text class="badge-letter" x="76" y="58" text-anchor="middle" fill="url(#silver)" stroke="#6e6e6e" stroke-width="1.5">A</text>
      </svg>
      <span class="choice-text">30 square meters</span>
    </li>
    <li class="choice">
      <svg class="choice-badge" viewBox="0 0 152 82" aria-label="Choice B">
        <ellipse cx="76" cy="74" rx="66" ry="7" fill="url(#drop)"/>
        <ellipse cx="76" cy="38" rx="72" ry="34" fill="url(#fill-blue)"/>
        <ellipse cx="76" cy="20" rx="54" ry="14" fill="url(#shine)"/>
        <text class="badge-letter" x="76" y="58" text-anchor="middle" fill="url(#silver)" stroke="#6e6e6e" stroke-width="1.5">B</text>
      </svg>
      <span class="choice-text">13 square meters</span>
    </li>
    <li class="choice">
      <svg class="choice-badge" viewBox="0 0 152 82" aria-label="Choice C">
        <ellipse cx="76" cy="74" rx="66" ry="7" fill="url(#drop)"/>
        <ellipse cx="76" cy="38" rx="72" ry="34" fill="url(#fill-gold)"/>
        <ellipse cx="76" cy="20" rx="54" ry="14" fill="url(#shine)"/>
        <text class="badge-letter" x="76" y="58" text-anchor="middle" fill="url(#silver)" stroke="#6e6e6e" stroke-width="1.5">C</text>
      </svg>
      <span class="choice-text">26 square meters</span>
    </li>
    <li class="choice">
      <svg class="choice-badge" viewBox="0 0 152 82" aria-label="Choice D">
        <ellipse cx="76" cy="74" rx="66" ry="7" fill="url(#drop)"/>
        <ellipse cx="76" cy="38" rx="72" ry="34" fill="url(#fill-green)"/>
        <ellipse cx="76" cy="20" rx="54" ry="14" fill="url(#shine)"/>
        <text class="badge-letter" x="76" y="58" text-anchor="middle" fill="url(#silver)" stroke="#6e6e6e" stroke-width="1.5">D</text>
      </svg>
      <span class="choice-text">40 square meters</span>
    </li>
  </ul>
</body>
</html>
```